SkyvoraQ Business Cards and Stationary Design

Need a design for our business cards and stationary. I want to carry on the theme of the logo. I want the business cards to have a design on the back. I would like the business cards and the stationary to carry the same theme, design scheme, and branding

Target Market(s)

Airlines and Maintenance Facilities

Industry/Entity Type

Aviation

Contact Information for Business Card

Name
Position Title
Address: 4827 Tollbeck Lane, Brennick Bay, Calder, 50917
Office Number
Mobile Number
Email
Website

Font styles to use
Serif
Sans Serif

Colors

Designer to choose colors to be used in the design.

```html
<!DOCTYPE html>
<html lang="en">
<head>
<meta charset="utf-8">
<title>SkyvoraQ Business Card</title>
<link rel="stylesheet" href="https://fonts.googleapis.com/css2?family=Orbitron:wght@600&family=Roboto:wght@400;500&display=swap">
<style>
  :root {
    --stage: #3b3b3d;
    --navy: #0c1830;
    --navy-soft: #13244a;
    --brand-blue: #1f5fc4;
    --ink: #16223a;
    --paper: #ffffff;
    --faint: #ececee;
    --white: #ffffff;
  }
  * { margin: 0; padding: 0; box-sizing: border-box; }
  html, body { width: 1200px; height: 712px; overflow: hidden; }
  body {
    background: var(--stage);
    font-family: "Roboto", Arial, sans-serif;
    position: relative;
  }
  .card {
    position: absolute;
    top: 206px;
    width: 520px;
    height: 300px;
    overflow: hidden;
    box-shadow: 0 14px 30px rgba(0,0,0,0.35);
  }
  .card-back { left: 50px; background: var(--navy); }
  .card-front { left: 630px; background: var(--paper); }

  .back-pattern {
    position: absolute; inset: 0;
    background: radial-gradient(circle at 50% 45%, var(--navy-soft) 0%, var(--navy) 75%);
  }
  .back-brand {
    position: absolute; left: 0; right: 0; top: 78px;
    display: flex; flex-direction: column; align-items: center; gap: 20px;
  }
  .back-mark {
    width: 78px; height: 78px; border-radius: 50%;
    border: 7px solid var(--white);
  }
  .back-name {
    font-family: "Orbitron", Arial, sans-serif;
    font-weight: 600;
    font-size: 34px; letter-spacing: 5px;
    color: var(--brand-blue);
  }

  .front-watermark {
    position: absolute; right: -50px; top: 36px;
    width: 240px; height: 240px; border-radius: 50%;
    border: 22px solid var(--faint);
  }
  .front-brand {
    position: absolute; left: 40px; top: 42px;
    display: flex; align-items: center; gap: 12px;
  }
  .front-mark {
    width: 52px; height: 52px; border-radius: 50%;
    border: 5px solid var(--brand-blue);
  }
  .front-name {
    font-family: "Orbitron", Arial, sans-serif;
    font-weight: 600;
    font-size: 22px; letter-spacing: 3px; color: var(--ink);
  }
  .person { position: absolute; left: 78px; top: 150px; }
  .person-name {
    font-family: "Orbitron", Arial, sans-serif;
    font-weight: 600;
    font-size: 17px; letter-spacing: 1px; color: var(--ink);
  }
  .person-role {
    margin-top: 6px;
    font-size: 10px; letter-spacing: 1px; color: var(--brand-blue);
  }
  .contact {
    position: absolute; left: 78px; top: 212px;
    padding-left: 14px;
    border-left: 3px solid var(--brand-blue);
    list-style: none;
    font-size: 11.5px; line-height: 16px; color: var(--ink); letter-spacing: 0.3px;
  }
</style>
</head>
<body>
  <section class="card card-back" aria-label="Card back">
    <div class="back-pattern" role="img" aria-label="Repeating brand pattern in dark navy tones"></div>
    <div class="back-brand">
      <div class="back-mark"></div>
      <div class="back-name">SKYVORAQ</div>
    </div>
  </section>

  <section class="card card-front" aria-label="Card front">
    <div class="front-watermark"></div>
    <div class="front-brand">
      <div class="front-mark"></div>
      <div class="front-name">SKYVORAQ</div>
    </div>
    <div class="person">
      <div class="person-name">DANA WHITLOW</div>
      <div class="person-role">DIRECTOR</div>
    </div>
    <ul class="contact">
      <li>0214865302</li>
      <li>info@skyvoraq.com</li>
      <li>www.skyvoraq.com</li>
      <li>4827 Tollbeck Lane, Brennick Bay, Calder, 50917</li>
    </ul>
  </section>
</body>
</html>
```